Colorful Live Music Concert Poster for Paper Lanterns

Looking for a portrait oriented "poster" promoting the band's upcoming show at Marlow Lounge on Sunday, 3/22 at 8 pm, and social version (square format for Instagram). <br/><br/>Copy:<br/>Paper Lanterns<br/>with The Quiet Tides<br/><br/>Marlow Lounge <br/>Sunday, March 22<br/>8 pm<br/><br/>Poster must be consistent with band's overall branding seen on www.paperlanternsmusic.example and it's Spotify page at https://music.example.net/artist/7QwErTy2uIoPaSdFgHjKl?si=123abcDEFghiJKLmnoPQrs <br/><br/>BUT, we wouldn't mind taking in a slightly updated direction. A good example is the cover for our recent single Blue Hours, which is consistent in theme and color palette while updating the design and color at the same time. <br/><br/>The attached files include some band logo art as well as examples of posters done for prior shows. <br/><br/>The posters need not include photos of the band, but if you are so inclined, we've uploaded some selects as well.<br/><br/>Thank you. <br/><br/>Martin<br/>Paper Lanterns

```html
<!DOCTYPE html>
<html lang="en">
<head>
<meta charset="utf-8">
<title>Paper Lanterns – Live at Marlow Lounge</title>
<link rel="stylesheet" href="https://fonts.googleapis.com/css2?family=Josefin+Sans:wght@400&family=Roboto+Condensed:wght@400;700&display=swap">
<style>
  :root {
    --navy: #232a55;
    --gold: #f8b100;
    --sky: #0096c9;
    --paper: #ffffff;
    --footer: #fafafa;
    --ink: #232a55;
    --text: #1e1e1e;
    --photo-wall: #ebe9e7;
    --photo-skin: #dcc3b0;
    --photo-shirt: #2c2f36;
    --photo-top: #f0b424;
    --photo-guitar: #eda044;
  }
  html, body {
    margin: 0;
    padding: 0;
    width: 1200px;
    height: 1200px;
    overflow: hidden;
    background: var(--paper);
  }
  .poster {
    position: relative;
    width: 1200px;
    height: 1200px;
    background: var(--paper);
    overflow: hidden;
  }
  .tile { position: absolute; }
  .tile--navy { background: var(--navy); }
  .tile--gold { background: var(--gold); }
  .tile--sky { background: var(--sky); }

  .photo--singer-face { background: linear-gradient(90deg, var(--photo-wall) 45%, var(--photo-skin) 100%); }
  .photo--guitarist-face { background: linear-gradient(90deg, var(--photo-skin) 0%, var(--photo-wall) 60%, var(--photo-top) 100%); }
  .photo--singer-shoulder { background: linear-gradient(90deg, var(--photo-top) 0%, var(--photo-wall) 100%); }
  .photo--guitar-body { background: linear-gradient(180deg, var(--photo-shirt) 0%, var(--photo-shirt) 60%, var(--photo-guitar) 100%); }
  .photo--singer-top { background: linear-gradient(180deg, var(--photo-top) 0%, #e7a91c 100%); }
  .photo--guitar-pickups { background: linear-gradient(90deg, var(--photo-guitar) 0%, #f2b763 100%); }
  .photo--guitar-neck { background: linear-gradient(180deg, var(--photo-wall) 0%, #4a3f3a 45%, var(--photo-shirt) 100%); }

  .footer {
    position: absolute;
    left: 0;
    top: 1058px;
    width: 1200px;
    height: 142px;
    background: var(--footer);
  }
  .band-name {
    position: absolute;
    left: 32px;
    top: 1086px;
    margin: 0;
    font-family: "Josefin Sans", sans-serif;
    font-weight: 400;
    font-size: 50px;
    letter-spacing: 4px;
    line-height: 1;
    color: var(--ink);
    white-space: nowrap;
  }
  .support-act {
    position: absolute;
    left: 600px;
    top: 1100px;
    margin: 0;
    font-family: "Roboto Condensed", sans-serif;
    font-weight: 400;
    font-size: 24px;
    line-height: 1;
    color: var(--text);
    white-space: nowrap;
  }
  .show-date {
    position: absolute;
    left: 33px;
    top: 1146px;
    margin: 0;
    font-family: "Roboto Condensed", sans-serif;
    font-weight: 700;
    font-size: 38px;
    line-height: 1;
    color: var(--text);
    letter-spacing: 0.5px;
    white-space: nowrap;
  }
  .venue {
    position: absolute;
    right: 20px;
    top: 1083px;
    margin: 0;
    font-family: "Roboto Condensed", sans-serif;
    font-weight: 400;
    font-style: normal;
    font-size: 26px;
    line-height: 34px;
    text-align: right;
    color: var(--text);
    white-space: nowrap;
  }
</style>
</head>
<body>
<main class="poster">
  <div class="tile tile--navy" style="left:0;top:6px;width:135px;height:196px"></div>
  <div class="tile tile--gold" style="left:152px;top:6px;width:532px;height:196px"></div>
  <div class="tile photo--singer-face" role="img" aria-label="Photo section: smiling singer with long brown hair" style="left:701px;top:6px;width:499px;height:196px"></div>

  <div class="tile tile--sky" style="left:0;top:220px;width:408px;height:196px"></div>
  <div class="tile photo--guitarist-face" role="img" aria-label="Photo section: guitarist in glasses beside the singer in a yellow top" style="left:425px;top:220px;width:531px;height:196px"></div>
  <div class="tile photo--singer-shoulder" role="img" aria-label="Photo section: singer's shoulder and yellow sleeve" style="left:972px;top:220px;width:228px;height:196px"></div>

  <div class="tile tile--sky" style="left:0;top:433px;width:134px;height:196px"></div>
  <div class="tile photo--guitar-body" role="img" aria-label="Photo section: guitarist's dark shirt above an orange guitar" style="left:150px;top:433px;width:531px;height:196px"></div>
  <div class="tile photo--singer-top" role="img" aria-label="Photo section: singer's yellow ribbed crop top" style="left:699px;top:433px;width:501px;height:196px"></div>

  <div class="tile photo--guitar-pickups" role="img" aria-label="Photo section: hand strumming an orange guitar" style="left:0;top:646px;width:419px;height:198px"></div>
  <div class="tile photo--guitar-neck" role="img" aria-label="Photo section: hand fretting the guitar neck" style="left:436px;top:646px;width:530px;height:198px"></div>
  <div class="tile tile--navy" style="left:984px;top:646px;width:216px;height:198px"></div>

  <div class="tile tile--gold" style="left:0;top:862px;width:159px;height:196px"></div>
  <div class="tile tile--navy" style="left:175px;top:862px;width:532px;height:196px"></div>
  <div class="tile tile--sky" style="left:724px;top:862px;width:476px;height:196px"></div>

  <footer class="footer"></footer>
  <h1 class="band-name">PAPER LANTERNS</h1>
  <p class="support-act">with The Quiet Tides</p>
  <p class="show-date">SUNDAY, MARCH 22 8PM</p>
  <address class="venue">Marlow Lounge<br>418 N Larkspur Ave.<br>Los Angeles, CA&nbsp; 90028</address>
</main>
</body>
</html>
```